Powepoint template for an investment group

Need high end clear clean concise creative luxurious

Have royal clients
High end/billionaire investors

Using ross gold logo can be creative
Must habe page numbers
Logo preference header top right
Page number footer bottom right

The first page of the ppt maybe a big block of dark grey and oberi investment group written on the front page in rose gold

Target Market(s)

Investors at a high level

Requirements
Must have
• Luxury feel

```html
<!DOCTYPE html>
<html lang="en">
<head>
<meta charset="utf-8">
<title>Oberi Investment Group – Presentation Template</title>
<link href="https://fonts.googleapis.com/css2?family=Ubuntu:wght@300;400;500&display=swap" rel="stylesheet">
<style>
  :root{
    --canvas:#d7d7d7;
    --stage:#e4e6ea;
    --charcoal:#242424;
    --rose:#b47468;
    --blush:#f3c6c0;
    --ink:#2a2a2a;
    --body:#3a3a3a;
    --white:#ffffff;
  }
  *{box-sizing:border-box;margin:0;padding:0}
  html,body{width:1200px;height:2754px;overflow:hidden}
  body{background:var(--canvas);font-family:"Ubuntu",sans-serif;color:var(--ink);position:relative}
  .hero{position:absolute;left:0;top:0;width:1200px;height:715px;background:var(--stage)}
  .hero-slide{transform:scale(1.4565);transform-origin:0 0;box-shadow:0 10px 30px rgba(0,0,0,.18)}
  .brand-tile{position:absolute;left:980px;top:0;width:155px;height:155px;background:var(--charcoal);display:flex;align-items:center;justify-content:center}
  .slide{position:absolute;width:563px;height:316px;background:var(--white);overflow:hidden}
  .slide.dark{background:var(--charcoal)}
  /* company name set as plain text with one square */
  .wordmark{display:flex;align-items:center;gap:.5em;color:var(--rose);font-weight:400;line-height:1.15;letter-spacing:0}
  .wordmark .mark-square{flex:none;width:.6em;height:.6em;background:var(--rose)}
  .wordmark .name{white-space:nowrap}
  .wordmark.wrap .name{white-space:normal}
  .header-logo{position:absolute;right:21px;top:0;width:72px;height:72px;background:var(--charcoal);display:flex;align-items:center;justify-content:center;font-size:7px}
  .header-logo .name{width:46px}
  .footer-band{position:absolute;left:0;bottom:0;width:100%;height:15px;background:var(--rose)}
  .page-number{position:absolute;right:14px;top:4px;font-size:5px;color:var(--white);letter-spacing:.05em}
  .heading{position:absolute;left:47px;top:46px;font-size:23px;font-weight:400;color:var(--ink)}
  .heading.on-dark{color:var(--rose)}
  .heading-rule{position:absolute;left:47px;top:80px;width:50px;height:3px;background:linear-gradient(90deg,var(--rose) 0 45%,var(--blush) 45% 100%)}
  .small{font-size:6.3px;line-height:1.3;color:var(--body)}
  .sub{font-size:10px;color:var(--rose)}
  .photo{position:absolute}
  .abs{position:absolute}
  .centered{position:absolute;left:0;right:0;display:flex;justify-content:center}
  /* title */
  .title-photo{left:0;top:0;width:158px;height:316px;background:linear-gradient(160deg,#a98077,#c5a099 50%,#9c756c)}
  .title-block{position:absolute;left:55px;top:55px;width:207px;height:206px;background:var(--charcoal);display:flex;align-items:center;justify-content:center;font-size:12px}
  .title-text{position:absolute;left:300px;top:90px;font-size:28px;line-height:1.12;color:var(--ink)}
  .title-sub{position:absolute;left:300px;top:157px;font-size:11.5px;color:var(--rose)}
  .date-bar{position:absolute;left:300px;top:204px;width:111px;height:15px;background:var(--rose);color:var(--white);font-size:6px;text-align:center;line-height:15px;letter-spacing:.06em}
  /* agenda */
  .agenda-item{position:absolute;width:200px;height:36px}
  .agenda-num{position:absolute;left:0;top:6px;font-size:19px;color:var(--white);font-weight:300}
  .agenda-rule{position:absolute;left:22px;top:0;width:1px;height:36px;background:var(--rose)}
  .agenda-title{position:absolute;left:32px;top:0;font-size:10px;color:var(--rose)}
  .agenda-body{position:absolute;left:32px;top:13px;width:150px;font-size:6.3px;line-height:1.3;color:#e6e6e6}
  /* bullets */
  .bullets{list-style:none}
  .bullets li{position:relative;padding-left:16px;margin-bottom:8px}
  .bullets li::before{content:"";position:absolute;left:1px;top:2px;width:3px;height:3px;border-radius:50%;background:var(--rose)}
  /* process */
  .step-box{position:absolute;top:131px;width:25px;height:25px;color:var(--white);font-size:15px;text-align:center;line-height:25px}
  .step-box.rose{background:var(--rose)}
  .step-box.blush{background:var(--blush)}
  .step-text{position:absolute;top:170px;width:74px;text-align:center;font-size:6px;line-height:1.25;color:var(--body)}
  /* icons */
  .icon-tile{position:absolute;width:34px;height:34px;background:var(--rose);display:flex;align-items:center;justify-content:center}
  /* contact */
  .contact-title{position:absolute;left:0;width:100%;top:187px;text-align:center;font-size:13px;color:var(--white)}
  .contact-pill{position:absolute;top:222px;width:148px;height:20px;border-radius:3px;background:var(--rose);color:var(--white);font-size:6px;line-height:20px}
  .contact-pill .pill-icon{position:absolute;left:3px;top:3px;width:20px;height:14px;border-radius:2px;background:rgba(255,255,255,.25);display:flex;align-items:center;justify-content:center}
  .contact-pill .pill-text{position:absolute;left:40px}
</style>
</head>
<body>

<section class="hero" aria-label="Title slide shown flat">
  <div class="slide hero-slide" style="left:130px;top:120px">
    <div class="photo title-photo" role="img" aria-label="Warm rose-toned photograph of hands at a laptop"></div>
    <div class="title-block"><div class="wordmark"><span class="mark-square"></span><span class="name">Oberi Investment Group</span></div></div>
    <div class="title-text">Presentation<br>Title Goes Here</div>
    <div class="title-sub">Subtitle of Presentation Goes Here</div>
    <div class="date-bar">October 31, 2022</div>
  </div>
  <div class="brand-tile" style="font-size:10px"><div class="wordmark"><span class="mark-square"></span><span class="name">Oberi Investment Group</span></div></div>
</section>

<!-- Slide 1: cover -->
<div class="slide dark" style="left:28px;top:729px">
  <div class="centered" style="top:140px;font-size:28px"><div class="wordmark"><span class="mark-square"></span><span class="name">Oberi Investment Group</span></div></div>
</div>

<!-- Slide 2: title -->
<div class="slide" style="left:610px;top:729px">
  <div class="photo title-photo" role="img" aria-label="Warm rose-toned photograph of hands at a laptop"></div>
  <div class="title-block"><div class="wordmark"><span class="mark-square"></span><span class="name">Oberi Investment Group</span></div></div>
  <div class="title-text">Presentation<br>Title Goes Here</div>
  <div class="title-sub">Subtitle of Presentation Goes Here</div>
  <div class="date-bar">October 31, 2022</div>
</div>

<!-- Slide 3: agenda -->
<div class="slide dark" style="left:28px;top:1064px">
  <div class="photo" role="img" aria-label="Faint dark photograph of a desk with a laptop" style="inset:0;background:radial-gradient(ellipse at 40% 70%,#363636,#252525 70%)"></div>
  <div class="header-logo"><div class="wordmark wrap"><span class="mark-square"></span><span class="name">Oberi Investment Group</span></div></div>
  <div class="heading on-dark">Agenda</div>
  <div class="heading-rule"></div>
  <div class="agenda-item" style="left:76px;top:117px"><span class="agenda-num">1</span><span class="agenda-rule"></span><span class="agenda-title">Lorem ipsum dolor sit amet</span><span class="agenda-body">Lorem ipsum dolor sit amet, consectetur adipiscing elit. Vivamus eu dui ex.</span></div>
  <div class="agenda-item" style="left:298px;top:117px"><span class="agenda-num">2</span><span class="agenda-rule"></span><span class="agenda-title">Lorem ipsum dolor sit amet</span><span class="agenda-body">Lorem ipsum dolor sit amet, consectetur adipiscing elit. Vivamus eu dui ex.</span></div>
  <div class="agenda-item" style="left:76px;top:172px"><span class="agenda-num">3</span><span class="agenda-rule"></span><span class="agenda-title">Lorem ipsum dolor sit amet</span><span class="agenda-body">Lorem ipsum dolor sit amet, consectetur adipiscing elit. Vivamus eu dui ex.</span></div>
  <div class="agenda-item" style="left:298px;top:172px"><span class="agenda-num">4</span><span class="agenda-rule"></span><span class="agenda-title">Lorem ipsum dolor sit amet</span><span class="agenda-body">Lorem ipsum dolor sit amet, consectetur adipiscing elit. Vivamus eu dui ex.</span></div>
  <div class="agenda-item" style="left:76px;top:227px"><span class="agenda-num">5</span><span class="agenda-rule"></span><span class="agenda-title">Lorem ipsum dolor sit amet</span><span class="agenda-body">Lorem ipsum dolor sit amet, consectetur adipiscing elit. Vivamus eu dui ex.</span></div>
  <div class="agenda-item" style="left:298px;top:227px"><span class="agenda-num">6</span><span class="agenda-rule"></span><span class="agenda-title">Lorem ipsum dolor sit amet</span><span class="agenda-body">Lorem ipsum dolor sit amet, consectetur adipiscing elit. Vivamus eu dui ex.</span></div>
  <div class="footer-band"><span class="page-number">PAGE &nbsp;|&nbsp; 3</span></div>
</div>

<!-- Slide 4: about -->
<div class="slide" style="left:610px;top:1064px">
  <div class="header-logo"><div class="wordmark wrap"><span class="mark-square"></span><span class="name">Oberi Investment Group</span></div></div>
  <div class="heading">About Us</div>
  <div class="heading-rule"></div>
  <div class="abs small" style="left:47px;top:123px;width:262px">
    <p style="margin-bottom:5px">Lorem ipsum dolor sit amet, consectetur adipiscing elit. Vivamus eu dui ex. Curabitur dapibus dignissim dui, in molestie metus feugiat sed. Praesent aliquet lorem ex, eu dapibus odio varius at. Duis eget tellus porta, consequat lacus vitae, venenatis dolor. Nulla facilisi. In et sollicitudin lacus.</p>
    <p style="margin-bottom:5px">Donec risus orci, gravida sit amet risus vehicula, aliquet pretium sapien. Nullam sit amet magna non ex bibendum mollis. Nunc vel neque eu augue dignissim congue ut vitae magna. Phasellus eget commodo arcu. Nunc vitae semper dui.</p>
    <p>Lorem ipsum dolor sit amet, consectetur adipiscing elit. Vivamus eu dui ex. Curabitur dapibus dignissim dui, in molestie metus feugiat sed. Praesent aliquet lorem ex, eu dapibus odio varius at. Duis eget tellus porta, consequat lacus vitae, venenatis dolor.</p>
  </div>
  <div class="photo" role="img" aria-label="Photograph of business people reviewing a chart on a tablet" style="left:337px;top:120px;width:179px;height:130px;background:linear-gradient(135deg,#d9dde2,#7d8590 55%,#3b4048)"></div>
  <div class="footer-band"><span class="page-number">PAGE &nbsp;|&nbsp; 4</span></div>
</div>

<!-- Slide 5: two columns -->
<div class="slide" style="left:28px;top:1399px">
  <div class="header-logo"><div class="wordmark wrap"><span class="mark-square"></span><span class="name">Oberi Investment Group</span></div></div>
  <div class="heading">Heading Goes Here</div>
  <div class="heading-rule"></div>
  <div class="abs" style="left:47px;top:119px;width:225px">
    <div class="sub" style="margin-bottom:9px">Heading Goes Here</div>
    <ul class="bullets small">
      <li>Lorem ipsum dolor sit amet, consectetur adipiscing elit. Vivamus eu dui ex. Curabitur dapibus dignissim dui, in molestie metus feugiat sed.</li>
      <li>Praesent aliquet lorem ex, eu dapibus odio varius at. Duis eget tellus porta, consequat lacus vitae, venenatis dolor. Nulla facilisi. In et sollicitudin lacus.</li>
      <li>Donec risus orci, gravida sit amet risus vehicula, aliquet pretium sapien. Nullam sit amet magna non ex bibendum mollis. Nunc vel neque eu augue dignissim congue ut vitae magna.</li>
    </ul>
  </div>
  <div class="abs" style="left:293px;top:119px;width:225px">
    <div class="sub" style="margin-bottom:9px">Heading Goes Here</div>
    <ul class="bullets small">
      <li>Lorem ipsum dolor sit amet, consectetur adipiscing elit. Vivamus eu dui ex. Curabitur dapibus dignissim dui, in molestie metus feugiat sed.</li>
      <li>Praesent aliquet lorem ex, eu dapibus odio varius at. Duis eget tellus porta, consequat lacus vitae, venenatis dolor. Nulla facilisi. In et sollicitudin lacus.</li>
      <li>Donec risus orci, gravida sit amet risus vehicula, aliquet pretium sapien. Nullam sit amet magna non ex bibendum mollis. Nunc vel neque eu augue dignissim congue ut vitae magna.</li>
    </ul>
  </div>
  <div class="footer-band"><span class="page-number">PAGE &nbsp;|&nbsp; 5</span></div>
</div>

<!-- Slide 6: three images -->
<div class="slide" style="left:610px;top:1399px">
  <div class="header-logo"><div class="wordmark wrap"><span class="mark-square"></span><span class="name">Oberi Investment Group</span></div></div>
  <div class="heading">Heading Goes Here</div>
  <div class="heading-rule"></div>
  <div class="photo" role="img" aria-label="Overhead photograph of a team meeting around a wooden table" style="left:47px;top:113px;width:153px;height:79px;background:linear-gradient(135deg,#8a6a52,#b08b6c 50%,#6e5a4c)"></div>
  <div class="photo" role="img" aria-label="Photograph of a hand with a pen over printed financial charts" style="left:208px;top:113px;width:153px;height:79px;background:linear-gradient(135deg,#f1f3f7,#d8dde6 60%,#c9b7b0)"></div>
  <div class="photo" role="img" aria-label="Photograph of hands reviewing paperwork together" style="left:369px;top:113px;width:153px;height:79px;background:linear-gradient(135deg,#5a4038,#d6d3d2 55%,#3e302b)"></div>
  <div class="abs" style="left:53px;top:201px;width:140px"><div class="sub" style="font-size:8.5px;margin-bottom:6px">Heading Goes Here</div><p class="small" style="font-size:6px">Lorem ipsum dolor sit amet, consectetur adipiscing elit. Vivamus eu dui ex. Curabitur dapibus dignissim dui, in molestie metus feugiat sed.</p></div>
  <div class="abs" style="left:214px;top:201px;width:140px"><div class="sub" style="font-size:8.5px;margin-bottom:6px">Heading Goes Here</div><p class="small" style="font-size:6px">Lorem ipsum dolor sit amet, consectetur adipiscing elit. Vivamus eu dui ex. Curabitur dapibus dignissim dui, in molestie metus feugiat sed.</p></div>
  <div class="abs" style="left:375px;top:201px;width:140px"><div class="sub" style="font-size:8.5px;margin-bottom:6px">Heading Goes Here</div><p class="small" style="font-size:6px">Lorem ipsum dolor sit amet, consectetur adipiscing elit. Vivamus eu dui ex. Curabitur dapibus dignissim dui, in molestie metus feugiat sed.</p></div>
  <div class="footer-band"><span class="page-number">PAGE &nbsp;|&nbsp; 6</span></div>
</div>

<!-- Slide 7: process -->
<div class="slide" style="left:28px;top:1734px">
  <div class="header-logo"><div class="wordmark wrap"><span class="mark-square"></span><span class="name">Oberi Investment Group</span></div></div>
  <div class="heading">Heading Goes Here</div>
  <div class="heading-rule"></div>
  <svg class="abs" style="left:0;top:138px" width="563" height="10" aria-hidden="true">
    <line x1="0" y1="5" x2="540" y2="5" stroke="#b8b8b8" stroke-width="1" stroke-dasharray="1.5 2"/>
    <path d="M538 2 L543 5 L538 8" fill="none" stroke="#b8b8b8" stroke-width="1"/>
  </svg>
  <div class="step-box rose" style="left:74px">1</div>
  <div class="step-box blush" style="left:170px">2</div>
  <div class="step-box rose" style="left:266px">3</div>
  <div class="step-box blush" style="left:361px">4</div>
  <div class="step-box rose" style="left:457px">5</div>
  <p class="step-text" style="left:49px">Lorem ipsum dolor sit amet, consectetur adipiscing elit. Vivamus eu dui ex. Curabitur dapibus dignissim dui, in molestie metus feugiat sed. Praesent aliquet lorem ex, eu dapibus odio varius at.</p>
  <p class="step-text" style="left:145px">Lorem ipsum dolor sit amet, consectetur adipiscing elit. Vivamus eu dui ex. Curabitur dapibus dignissim dui, in molestie metus feugiat sed. Praesent aliquet lorem ex, eu dapibus odio varius at.</p>
  <p class="step-text" style="left:241px">Lorem ipsum dolor sit amet, consectetur adipiscing elit. Vivamus eu dui ex. Curabitur dapibus dignissim dui, in molestie metus feugiat sed. Praesent aliquet lorem ex, eu dapibus odio varius at.</p>
  <p class="step-text" style="left:336px">Lorem ipsum dolor sit amet, consectetur adipiscing elit. Vivamus eu dui ex. Curabitur dapibus dignissim dui, in molestie metus feugiat sed. Praesent aliquet lorem ex, eu dapibus odio varius at.</p>
  <p class="step-text" style="left:432px">Lorem ipsum dolor sit amet, consectetur adipiscing elit. Vivamus eu dui ex. Curabitur dapibus dignissim dui, in molestie metus feugiat sed. Praesent aliquet lorem ex, eu dapibus odio varius at.</p>
  <div class="footer-band"><span class="page-number">PAGE &nbsp;|&nbsp; 7</span></div>
</div>

<!-- Slide 8: pyramid -->
<div class="slide" style="left:610px;top:1734px">
  <div class="header-logo"><div class="wordmark wrap"><span class="mark-square"></span><span class="name">Oberi Investment Group</span></div></div>
  <div class="heading">Heading Goes Here</div>
  <div class="heading-rule"></div>
  <svg class="abs" style="left:0;top:0" width="563" height="316" aria-hidden="true">
    <polygon points="280,110 250,148 280,160" fill="#b47468"/><polygon points="280,110 310,148 280,160" fill="#9c6257"/>
    <polygon points="248,151 280,164 280,182 232,170" fill="#9b9b9b"/><polygon points="312,151 280,164 280,182 328,170" fill="#7d7d7d"/>
    <polygon points="246,156 280,169 280,194 228,178" fill="#f5cdc8"/><polygon points="314,156 280,169 280,194 332,178" fill="#f0b8b1"/>
    <polygon points="226,183 280,203 280,228 206,200" fill="#8e8e8e"/><polygon points="334,183 280,203 280,228 354,200" fill="#6f6f6f"/>
    <polygon points="224,188 280,209 280,247 200,217" fill="#2b2b2b"/><polygon points="336,188 280,209 280,247 360,217" fill="#1c1c1c"/>
    <line x1="321" y1="127" x2="360" y2="127" stroke="#9a9a9a" stroke-width=".6"/>
    <line x1="198" y1="167" x2="235" y2="167" stroke="#9a9a9a" stroke-width=".6"/>
    <line x1="335" y1="236" x2="360" y2="236" stroke="#9a9a9a" stroke-width=".6"/>
    <line x1="160" y1="145" x2="160" y2="205" stroke="#f3c6c0" stroke-width="1.5"/>
    <line x1="390" y1="102" x2="390" y2="162" stroke="#b47468" stroke-width="1.5"/>
    <line x1="390" y1="210" x2="390" y2="270" stroke="#242424" stroke-width="1.5"/>
    <rect x="360" y="117" width="21" height="21" fill="#b47468"/>
    <circle cx="370.5" cy="125" r="4" fill="none" stroke="#fff" stroke-width="1.2"/><rect x="368.5" y="129.5" width="4" height="3" fill="#fff"/>
    <rect x="175" y="157" width="23" height="21" fill="#f3c6c0"/>
    <circle cx="182" cy="165" r="2" fill="#fff"/><circle cx="191" cy="165" r="2" fill="#fff"/><circle cx="186.5" cy="164" r="2.3" fill="#fff"/><rect x="180" y="168" width="13" height="4" rx="2" fill="#fff"/>
    <rect x="360" y="225" width="21" height="21" fill="#242424"/>
    <circle cx="370.5" cy="235.5" r="4.5" fill="none" stroke="#fff" stroke-width="2" stroke-dasharray="2 1.4"/><circle cx="370.5" cy="235.5" r="1.6" fill="#fff"/>
  </svg>
  <div class="abs" style="left:40px;top:145px;width:113px;text-align:right"><div style="font-size:8.5px;margin-bottom:7px">Title Goes Here</div><p class="small" style="font-size:6px">Lorem ipsum dolor sit amet, consectetur adipiscing elit. Vivamus eu dui ex. Curabitur dapibus dignissim dui, in molestie metus feugiat sed.</p></div>
  <div class="abs" style="left:398px;top:105px;width:110px"><div style="font-size:8.5px;margin-bottom:7px">Title Goes Here</div><p class="small" style="font-size:6px">Lorem ipsum dolor sit amet, consectetur adipiscing elit. Vivamus eu dui ex. Curabitur dapibus dignissim dui, in molestie metus feugiat sed.</p></div>
  <div class="abs" style="left:398px;top:214px;width:110px"><div style="font-size:8.5px;margin-bottom:7px">Title Goes Here</div><p class="small" style="font-size:6px">Lorem ipsum dolor sit amet, consectetur adipiscing elit. Vivamus eu dui ex. Curabitur dapibus dignissim dui, in molestie metus feugiat sed.</p></div>
  <div class="footer-band"><span class="page-number">PAGE &nbsp;|&nbsp; 8</span></div>
</div>

<!-- Slide 9: icon features -->
<div class="slide" style="left:28px;top:2069px">
  <div class="header-logo"><div class="wordmark wrap"><span class="mark-square"></span><span class="name">Oberi Investment Group</span></div></div>
  <div class="heading">Heading Goes Here</div>
  <div class="heading-rule"></div>
  <div class="icon-tile" style="left:48px;top:125px"><svg width="18" height="20" viewBox="0 0 18 20" aria-hidden="true"><circle cx="9" cy="7.5" r="6" fill="none" stroke="#fff" stroke-width="1.6"/><rect x="6.5" y="14" width="5" height="4" fill="#fff"/></svg></div>
  <div class="icon-tile" style="left:288px;top:125px"><svg width="22" height="16" viewBox="0 0 22 16" aria-hidden="true"><circle cx="5" cy="5" r="2.6" fill="#fff"/><circle cx="17" cy="5" r="2.6" fill="#fff"/><circle cx="11" cy="4" r="3" fill="#fff"/><rect x="2" y="9" width="18" height="5" rx="2.5" fill="#fff"/></svg></div>
  <div class="icon-tile" style="left:48px;top:189px"><svg width="20" height="18" viewBox="0 0 20 18" aria-hidden="true"><rect x="2" y="12" width="3.5" height="5" fill="#fff"/><rect x="7" y="9" width="3.5" height="8" fill="#fff"/><rect x="12" y="5" width="3.5" height="12" fill="#fff"/><path d="M2 9 L9 4 L12 6 L18 1" fill="none" stroke="#fff" stroke-width="1.3"/></svg></div>
  <div class="icon-tile" style="left:288px;top:189px"><svg width="18" height="20" viewBox="0 0 18 20" aria-hidden="true"><path d="M6 2 H12 L10 6 H8 Z" fill="#fff"/><circle cx="9" cy="12.5" r="6.5" fill="#fff"/><text x="9" y="16" text-anchor="middle" font-size="9" font-family="Ubuntu, sans-serif" fill="#b47468">$</text></svg></div>
  <div class="abs" style="left:100px;top:123px;width:165px"><div class="sub" style="font-size:8.5px;margin-bottom:3px">Heading Goes Here</div><p class="small" style="font-size:6px">Lorem ipsum dolor sit amet, consectetur adipiscing elit. Vivamus eu dui ex. Curabitur dapibus dignissim dui, in molestie metus feugiat sed. Praesent aliquet lorem ex, eu dapibus odio varius at.</p></div>
  <div class="abs" style="left:340px;top:123px;width:165px"><div class="sub" style="font-size:8.5px;margin-bottom:3px">Heading Goes Here</div><p class="small" style="font-size:6px">Lorem ipsum dolor sit amet, consectetur adipiscing elit. Vivamus eu dui ex. Curabitur dapibus dignissim dui, in molestie metus feugiat sed. Praesent aliquet lorem ex, eu dapibus odio varius at.</p></div>
  <div class="abs" style="left:100px;top:187px;width:165px"><div class="sub" style="font-size:8.5px;margin-bottom:3px">Heading Goes Here</div><p class="small" style="font-size:6px">Lorem ipsum dolor sit amet, consectetur adipiscing elit. Vivamus eu dui ex. Curabitur dapibus dignissim dui, in molestie metus feugiat sed. Praesent aliquet lorem ex, eu dapibus odio varius at.</p></div>
  <div class="abs" style="left:340px;top:187px;width:165px"><div class="sub" style="font-size:8.5px;margin-bottom:3px">Heading Goes Here</div><p class="small" style="font-size:6px">Lorem ipsum dolor sit amet, consectetur adipiscing elit. Vivamus eu dui ex. Curabitur dapibus dignissim dui, in molestie metus feugiat sed. Praesent aliquet lorem ex, eu dapibus odio varius at.</p></div>
  <div class="footer-band"><span class="page-number">PAGE &nbsp;|&nbsp; 9</span></div>
</div>

<!-- Slide 10: bar chart -->
<div class="slide" style="left:610px;top:2069px">
  <div class="header-logo"><div class="wordmark wrap"><span class="mark-square"></span><span class="name">Oberi Investment Group</span></div></div>
  <div class="heading">Heading Goes Here</div>
  <div class="heading-rule"></div>
  <svg class="abs" style="left:0;top:0" width="563" height="316" role="img" aria-label="Monthly bar chart comparing Trend 01 and Trend 02">
    <g stroke="#e6e6e6" stroke-width=".5">
      <line x1="60" y1="250" x2="505" y2="250"/><line x1="60" y1="236" x2="505" y2="236"/><line x1="60" y1="222" x2="505" y2="222"/><line x1="60" y1="208" x2="505" y2="208"/><line x1="60" y1="194" x2="505" y2="194"/><line x1="60" y1="180" x2="505" y2="180"/><line x1="60" y1="166" x2="505" y2="166"/><line x1="60" y1="152" x2="505" y2="152"/><line x1="60" y1="138" x2="505" y2="138"/><line x1="60" y1="124" x2="505" y2="124"/><line x1="60" y1="110" x2="505" y2="110"/>
    </g>
    <g font-family="Ubuntu, sans-serif" font-size="5.5" fill="#555" text-anchor="end">
      <text x="56" y="252">0</text><text x="56" y="238">0.5</text><text x="56" y="224">1</text><text x="56" y="210">1.5</text><text x="56" y="196">2</text><text x="56" y="182">2.5</text><text x="56" y="168">3</text><text x="56" y="154">3.5</text><text x="56" y="140">4</text><text x="56" y="126">4.5</text><text x="56" y="112">5</text>
    </g>
    <g fill="#b47468">
      <rect x="70" y="130" width="8" height="120"/><rect x="107" y="183" width="8" height="67"/><rect x="143" y="155" width="8" height="95"/><rect x="180" y="127" width="8" height="123"/><rect x="217" y="132" width="8" height="118"/><rect x="253" y="183" width="8" height="67"/><rect x="290" y="155" width="8" height="95"/><rect x="327" y="127" width="8" height="123"/><rect x="363" y="132" width="8" height="118"/><rect x="400" y="183" width="8" height="67"/><rect x="437" y="155" width="8" height="95"/><rect x="473" y="127" width="8" height="123"/>
    </g>
    <g fill="#f3c6c0">
      <rect x="79" y="186" width="8" height="64"/><rect x="116" y="130" width="8" height="120"/><rect x="152" y="202" width="8" height="48"/><rect x="189" y="172" width="8" height="78"/><rect x="226" y="186" width="8" height="64"/><rect x="262" y="130" width="8" height="120"/><rect x="299" y="202" width="8" height="48"/><rect x="336" y="172" width="8" height="78"/><rect x="372" y="186" width="8" height="64"/><rect x="409" y="130" width="8" height="120"/><rect x="446" y="202" width="8" height="48"/><rect x="482" y="172" width="8" height="78"/>
    </g>
    <g font-family="Ubuntu, sans-serif" font-size="5.5" fill="#555" text-anchor="middle">
      <text x="78" y="261">JAN</text><text x="115" y="261">FEB</text><text x="151" y="261">MAR</text><text x="188" y="261">APR</text><text x="225" y="261">MAY</text><text x="261" y="261">JUN</text><text x="298" y="261">JUL</text><text x="335" y="261">AUG</text><text x="371" y="261">SEP</text><text x="408" y="261">OCT</text><text x="445" y="261">NOV</text><text x="481" y="261">DEC</text>
    </g>
    <rect x="246" y="268" width="3" height="3" fill="#b47468"/><text x="251" y="271" font-family="Ubuntu, sans-serif" font-size="5.5" fill="#555">Trend 01</text>
    <rect x="286" y="268" width="3" height="3" fill="#f3c6c0"/><text x="291" y="271" font-family="Ubuntu, sans-serif" font-size="5.5" fill="#555">Trend 02</text>
  </svg>
  <div class="footer-band"><span class="page-number">PAGE &nbsp;|&nbsp; 10</span></div>
</div>

<!-- Slide 11: contact -->
<div class="slide dark" style="left:319px;top:2404px">
  <div class="photo" role="img" aria-label="Faint dark photograph of a desk with a laptop" style="inset:0;background:radial-gradient(ellipse at 50% 80%,#363636,#262626 70%)"></div>
  <div class="centered" style="top:100px;font-size:26px"><div class="wordmark"><span class="mark-square"></span><span class="name">Oberi Investment Group</span></div></div>
  <div class="contact-title">Contact Us</div>
  <div class="contact-pill" style="left:51px"><span class="pill-icon"><svg width="10" height="10" viewBox="0 0 10 10" aria-hidden="true"><path d="M2 1 L4 1 L4.8 3 L3.6 4 Q4.5 6 6 6.6 L7 5.4 L9 6.2 L9 8 Q9 9 8 9 Q1 8.5 1 2 Q1 1 2 1Z" fill="#fff"/></svg></span><span class="pill-text">Insert Phone Number Here</span></div>
  <div class="contact-pill" style="left:207px"><span class="pill-icon"><svg width="10" height="10" viewBox="0 0 10 10" aria-hidden="true"><path d="M1 5 L9 1 L7 9 L5 6 Z" fill="none" stroke="#fff" stroke-width=".9"/></svg></span><span class="pill-text">Insert E-Mail Address Here</span></div>
  <div class="contact-pill" style="left:363px"><span class="pill-icon"><svg width="10" height="10" viewBox="0 0 10 10" aria-hidden="true"><circle cx="5" cy="5" r="4" fill="none" stroke="#fff" stroke-width=".9"/><ellipse cx="5" cy="5" rx="1.8" ry="4" fill="none" stroke="#fff" stroke-width=".7"/><line x1="1" y1="5" x2="9" y2="5" stroke="#fff" stroke-width=".7"/></svg></span><span class="pill-text">Insert URL Address Here</span></div>
</div>

</body>
</html>
```